Amber Ridge Ventures, LLC Business Card

We need a logo that will be embossed or printed in a singular light color for Business Cards. Would be interested in seeing a Cypress Tree graphic. Our company name is Amber Ridge Ventures, LLC. Business Card layout and graphic should project imagine of confidence, integrity and strength.

```html
<!DOCTYPE html>
<html lang="en">
<head>
<meta charset="utf-8">
<title>Amber Ridge Ventures, LLC – Business Card</title>
<link rel="stylesheet" href="https://fonts.googleapis.com/css2?family=Didact+Gothic&display=swap">
<style>
  :root {
    --backdrop: #e9e6e1;
    --card-light: #f4f4f4;
    --card-light-edge: #ffffff;
    --card-dark-top: #555555;
    --card-dark-bottom: #2e2e2e;
    --ink: #3a3a3a;
    --ink-soft: #5a5a5a;
    --ink-reverse: #f2f2f2;
    --mark: #4a4a4a;
    --rule: #444444;
  }
  * { margin: 0; padding: 0; box-sizing: border-box; }
  html, body { width: 1200px; height: 940px; overflow: hidden; }
  body {
    background: var(--backdrop);
    font-family: "Didact Gothic", "Century Gothic", sans-serif;
    color: var(--ink);
    position: relative;
  }
  .card {
    position: absolute;
    top: 170px;
    width: 350px;
    height: 600px;
    box-shadow: 0 10px 28px rgba(0,0,0,.18);
  }
  .card--front {
    left: 230px;
    background: radial-gradient(ellipse at 50% 20%, var(--card-light-edge), var(--card-light) 70%);
  }
  .card--back {
    left: 620px;
    background: linear-gradient(180deg, var(--card-dark-top), var(--card-dark-bottom) 75%);
  }
  .brand-mark {
    position: absolute;
    top: 40px;
    left: 50%;
    width: 72px;
    height: 72px;
    margin-left: -36px;
    border-radius: 50%;
    background: var(--mark);
  }
  .wordmark {
    position: absolute;
    left: 0; right: 0;
    text-align: center;
    text-transform: uppercase;
    line-height: 1;
  }
  .wordmark__name { display: block; font-size: 32px; letter-spacing: .5px; }
  .wordmark__suffix { display: block; font-size: 13px; letter-spacing: 5px; margin-top: 8px; }
  .card--front .wordmark { top: 134px; color: var(--ink); }
  .card--back .wordmark { top: 80px; color: var(--ink-reverse); }
  .holder {
    position: absolute;
    top: 320px; left: 0; right: 0;
    text-align: center;
  }
  .holder__name { font-size: 27px; color: var(--ink); }
  .holder__surname { text-transform: uppercase; }
  .holder__title { font-size: 13px; color: var(--ink-soft); margin-top: 4px; }
  .contact {
    position: absolute;
    top: 470px; left: 0; right: 0;
    text-align: center;
    font-size: 13.5px;
    line-height: 1.3;
    color: var(--ink-soft);
    font-style: normal;
  }
  .contact__label { font-weight: bold; color: var(--ink); }
  .contact__rule {
    display: block;
    width: 170px;
    height: 3px;
    background: var(--rule);
    margin: 8px auto 0;
  }
</style>
</head>
<body>
  <section class="card card--front" aria-label="Business card front">
    <span class="brand-mark" aria-hidden="true"></span>
    <div class="wordmark">
      <span class="wordmark__name">Amber Ridge</span>
      <span class="wordmark__suffix">Ventures, LLC</span>
    </div>
    <div class="holder">
      <p class="holder__name">Helena <span class="holder__surname">Morris</span></p>
      <p class="holder__title">Managing Partner</p>
    </div>
    <address class="contact">
      Lindenweg 42<br>
      CH-3012 Bern<br>
      <span class="contact__label">Tel:</span> +41 31 555 01 23<br>
      www.arventures.com
      <span class="contact__rule"></span>
    </address>
  </section>

  <section class="card card--back" aria-label="Business card back">
    <div class="wordmark">
      <span class="wordmark__name">Amber Ridge</span>
      <span class="wordmark__suffix">Ventures, LLC</span>
    </div>
  </section>
</body>
</html>
```